Vellora Trae - flyer for launch of new App with Web platform & Beacon support

Create an e-flyer for the new launch of Museum Web / App / Beacon platform for museum content delivery, management, experience and analytics.
The features of the product are contained in the pdf file uploaded for content and style guidance.
The e-flyer will be used as a mail drop and at conference events.

Target Market(s)

Museum owners, curators, innovation departments and potential sponsors.

Industry/Entity Type

Museum

Font styles to use
Other font styles liked:
• Presentation DIN Alternate or similar

Requirements
Must have
• Clear value proposition.
Nice to have
• Simple smart beacon explanation on how the technology links together.
• Web platform provides content management data to the App which then communicates with beacons located strategically inside the museum and relates to the user settings in the App (age, language, interests) to create a targeted experience.
Should not have
• Complexity and a lot of wording.

```html
<!DOCTYPE html>
<html lang="en">
<head>
<meta charset="utf-8">
<title>Vellora Trae – Museum Beacon Platform</title>
<link rel="stylesheet" href="https://fonts.googleapis.com/css2?family=Barlow:wght@400;500;600&family=Barlow+Semi+Condensed:wght@400;500&family=Open+Sans:wght@400;600&display=swap">
<style>
  :root{
    --stage:#d9d9d9;
    --charcoal:#363636;
    --crimson:#c41f30;
    --mist:#e6e7e8;
    --ink:#0e0e0e;
    --teal:#3dbf9a;
    --lagoon:#27a9bb;
    --sky:#2aa3c4;
    --text:#333333;
    --white:#ffffff;
  }
  *{margin:0;padding:0;box-sizing:border-box}
  html,body{width:691px;height:1200px;overflow:hidden;background:var(--stage)}
  .flyer{position:absolute;left:115px;top:0;width:460px;height:1200px;background:var(--white);font-family:"Barlow",sans-serif;color:var(--text)}
  .flyer section{position:absolute;left:0;width:460px}

  .hero{top:0;height:237px;background:var(--charcoal);color:var(--white);text-align:center}
  .brand{position:absolute;left:178px;top:28px;width:103px;height:103px;border-radius:50%;background:#000;border:2px solid var(--white);display:flex;align-items:center;justify-content:center;font-size:13px;font-weight:500;letter-spacing:.5px}
  .hero-line{position:absolute;top:143px;left:0;width:100%;font-family:"Barlow Semi Condensed",sans-serif;font-weight:500;font-size:13.5px;line-height:19px;text-transform:uppercase}
  .hero-line em{font-style:normal;color:var(--crimson)}

  .pricing{top:239px;height:70px;background:var(--crimson);color:var(--white);text-align:center;font-family:"Barlow Semi Condensed",sans-serif;font-weight:500}
  .pricing .label{margin-top:10px;font-size:15.5px}
  .pricing .price{font-size:21px;font-weight:500;margin-top:1px}

  .explainer{top:311px;height:139px;background:var(--mist)}
  .explainer .badge{position:absolute;left:45px;top:22px;width:94px;height:94px;border-radius:50%;background:var(--teal)}
  .explainer h2{position:absolute;left:150px;top:28px;font-size:16.5px;font-weight:600;color:#111}
  .explainer p{position:absolute;left:150px;top:50px;width:288px;font-family:"Open Sans",sans-serif;font-size:7px;line-height:9.6px;text-align:justify;color:#222}

  .process{top:450px;height:486px;background:var(--white)}
  .process h2{position:absolute;left:0;width:100%;top:16px;text-align:center;font-weight:500;font-size:21px;color:var(--crimson)}
  .scene{position:absolute;left:22px;top:58px;width:416px;height:177px;background:linear-gradient(180deg,#2bb0c2,#1f9fb2)}
  .scene-title{position:absolute;left:0;width:100%;top:14px;text-align:center;font-family:"Open Sans",sans-serif;font-weight:600;font-size:15px;color:var(--white)}
  .scene-caption{position:absolute;left:0;width:100%;top:250px;text-align:center;font-family:"Open Sans",sans-serif;font-size:13px;color:#444}
  .step{position:absolute;top:297px;width:110px;height:110px;border-radius:50%}
  .step-1{left:29px;background:var(--teal)}
  .step-2{left:175px;background:var(--sky)}
  .step-3{left:321px;background:var(--crimson)}
  .step-arrow{position:absolute;top:336px;width:22px;height:16px}
  .step-arrow.a1{left:144px}.step-arrow.a2{left:290px}
  .step-note{position:absolute;top:420px;width:130px;text-align:center;font-family:"Open Sans",sans-serif;font-size:8px;line-height:10.5px;color:#333}
  .n1{left:19px}.n2{left:165px}.n3{left:311px}

  .features{top:936px;height:145px;background:var(--crimson);color:var(--white)}
  .features ul{list-style:none}
  .features li{position:absolute;font-family:"Open Sans",sans-serif;font-size:13px;line-height:16px;padding-left:9px}
  .features li::before{content:"";position:absolute;left:0;top:6px;width:4px;height:4px;border-radius:50%;background:var(--white)}

  .contact{top:1085px;height:115px;background:var(--ink);color:var(--white);border-top:0}
  .contact h2{position:absolute;top:9px;width:100%;text-align:center;font-weight:500;font-size:18.5px}
  .contact-item{position:absolute;top:50px;display:flex;align-items:center;gap:8px;font-family:"Open Sans",sans-serif;font-size:8.8px}
  .contact-item svg{width:19px;height:19px;flex:none}
  .footnote{position:absolute;top:99px;width:100%;text-align:center;font-family:"Open Sans",sans-serif;font-size:6px;color:#aaa;text-transform:uppercase}
</style>
</head>
<body>
<main class="flyer">
  <section class="hero">
    <div class="brand">Vellora Trae</div>
    <p class="hero-line">Museums anchor us to the past, question our present<br>and pull us into the future. While technology opens our<br>world to new possibilities now <em>Vellora Trae</em> brings<br>you both in a brilliantly simple open platform</p>
  </section>

  <section class="pricing">
    <p class="label">INCREDIBLE ACCESS PRICING</p>
    <p class="price">$500 PER MONTH*</p>
  </section>

  <section class="explainer">
    <div class="badge">
      <svg viewBox="0 0 94 94" width="94" height="94" aria-hidden="true">
        <g fill="none" stroke="#1d2b3a" stroke-width="3" stroke-linecap="round">
          <path d="M47 40 L38 70 M47 40 L56 70 M41 58 L53 58"/>
          <path d="M38 28 a12 12 0 0 0 0 16 M56 28 a12 12 0 0 1 0 16" stroke="#fff" stroke-width="2"/>
          <path d="M33 24 a18 18 0 0 0 0 24 M61 24 a18 18 0 0 1 0 24" stroke="#fff" stroke-width="2"/>
        </g>
        <circle cx="47" cy="36" r="4.5" fill="#e8415a"/>
      </svg>
    </div>
    <h2>What Is Beacon Technology</h2>
    <p>Beacon platform enables contextual experiences for your users through interactions with Bluetooth low energy (BLE) beacons. Beacons are simple devices that send one-way BLE signals. These signals can be read by nearby Bluetooth-enabled devices. Beacons can be deployed at fixed places such as airports, museums, and bus stops, and attached to movable objects such as bicycles and taxis.</p>
  </section>

  <section class="process">
    <h2>How Beacon Technology Works With Museum</h2>
    <div class="scene" role="img" aria-label="Illustration of visitors in a museum gallery with a statue, vases, framed paintings and beacons on the walls">
      <p class="scene-title">Museum Exposure</p>
    </div>
    <p class="scene-caption">Beacons are placed strategically inside the museum</p>

    <div class="step step-1">
      <svg viewBox="0 0 110 110" width="110" height="110" aria-hidden="true">
        <g fill="none" stroke-linecap="round">
          <path d="M55 44 L45 80 M55 44 L65 80 M48 66 L62 66" stroke="#1d2b3a" stroke-width="3.5"/>
          <path d="M45 32 a14 14 0 0 0 0 18 M65 32 a14 14 0 0 1 0 18 M39 27 a21 21 0 0 0 0 28 M71 27 a21 21 0 0 1 0 28" stroke="#fff" stroke-width="2.2"/>
        </g>
        <circle cx="55" cy="41" r="5" fill="#e8415a"/>
      </svg>
    </div>
    <svg class="step-arrow a1" viewBox="0 0 22 16" aria-hidden="true"><path d="M2 13 Q8 3 16 5" fill="none" stroke="#111" stroke-width="2.5"/><path d="M13 1 L20 5 L13 10 Z" fill="#111"/></svg>
    <div class="step step-2" role="img" aria-label="Illustration of a hand holding a phone receiving a Bluetooth signal"></div>
    <svg class="step-arrow a2" viewBox="0 0 22 16" aria-hidden="true"><path d="M2 13 Q8 3 16 5" fill="none" stroke="#111" stroke-width="2.5"/><path d="M13 1 L20 5 L13 10 Z" fill="#111"/></svg>
    <div class="step step-3" role="img" aria-label="Illustration of a hand holding a phone showing a museum tour map"></div>

    <p class="step-note n1">Beacons connect to<br>visitors Bluetooth<br>enabled device</p>
    <p class="step-note n2">Signal is sent to<br>the device App<br>to get started</p>
    <p class="step-note n3">Museum creates a<br>targeted interactive experience<br>with informative tour</p>
  </section>

  <section class="features">
    <ul>
      <li style="left:16px;top:28px">Multiple<br>Language</li>
      <li style="left:125px;top:28px">Tailored<br>Interface</li>
      <li style="left:229px;top:28px">3d accurate<br>Broadcasting</li>
      <li style="left:351px;top:28px">Visitor<br>Targeted</li>
      <li style="left:16px;top:75px">Age Range<br>Specific<br>Learning</li>
      <li style="left:125px;top:75px">Revenue<br>Guided<br>Tours</li>
      <li style="left:229px;top:75px">Visitor<br>Behaviour<br>Reporting</li>
      <li style="left:351px;top:75px">Information<br>Smart Event<br>Reminders</li>
    </ul>
  </section>

  <section class="contact">
    <h2>Contact Us</h2>
    <div class="contact-item" style="left:18px">
      <svg viewBox="0 0 20 20" aria-hidden="true"><circle cx="10" cy="10" r="9" fill="none" stroke="#fff" stroke-width="1.2"/><path d="M7 5.5 L8.6 8 L7.6 9 Q8.6 11.4 11 12.4 L12 11.4 L14.5 13 L13.4 14.5 Q9 14.5 5.5 9.5 Q5.5 6.6 7 5.5 Z" fill="#fff"/></svg>
      <span>+44 (0)20 7946 0321</span>
    </div>
    <div class="contact-item" style="left:156px">
      <svg viewBox="0 0 20 20" aria-hidden="true"><circle cx="10" cy="10" r="9" fill="none" stroke="#fff" stroke-width="1.2"/><g fill="none" stroke="#fff" stroke-width="1"><circle cx="10" cy="10" r="5"/><ellipse cx="10" cy="10" rx="2.2" ry="5"/><path d="M5 10 H15"/></g></svg>
      <span>www.harbourlane.co.uk</span>
    </div>
    <div class="contact-item" style="left:315px">
      <svg viewBox="0 0 20 20" aria-hidden="true"><circle cx="10" cy="10" r="9" fill="none" stroke="#fff" stroke-width="1.2"/><rect x="5.5" y="6.8" width="9" height="6.4" fill="none" stroke="#fff" stroke-width="1"/><path d="M5.5 6.8 L10 10.5 L14.5 6.8" fill="none" stroke="#fff" stroke-width="1"/></svg>
      <span>info@harbourlane.co.uk</span>
    </div>
    <p class="footnote">*Basic visitor package + smart beacons $50/unit</p>
  </section>
</main>
</body>
</html>
```